Need Help having my business card stand out

I am the owner of Brisa Canine Coaching and would like for my business cards to stand out. I have been trying to keep designing them myself but I can't get what I have in my head on the card. I will try my best to post templates that I like for inspirations. I want something unique but elegant. I don't want in to look cartoony or cheesy. It needs to pop in a pet shop but also in a coffee shop or gym.

Target Market(s)

Dog owners, Married ,No young kids Jr High school kids and up (maybe kids on the way) Executives, Stay at home moms/wives, Small business owners

Industry/Entity Type

Dog Training

Contact Information for Business Card

Lorna Whitfield, 555-304-7719, info@brisacanine.example, www.brisacanine.example

Colors

Designer to choose colors to be used in the design.

Requirements
Must have
• my logo
Should not have
• Cursive lettering

```html
<!DOCTYPE html>
<html lang="en">
<head>
<meta charset="utf-8">
<title>Brisa Canine Coaching – Business Card</title>
<link rel="stylesheet" href="https://fonts.googleapis.com/css2?family=Oswald:wght@300;500&family=Crimson+Text:wght@400&display=swap">
<style>
  :root {
    --backdrop: #5a5a5c;
    --card: #ffffff;
    --ink: #141414;
    --ink-soft: #262626;
    --brand-blue: #0c3aa6;
    --on-blue: #ffffff;
    --card-radius: 30px;
  }
  * { box-sizing: border-box; margin: 0; padding: 0; }
  html, body { width: 1200px; height: 1000px; overflow: hidden; }
  body {
    background: var(--backdrop);
    position: relative;
    font-family: "Crimson Text", Georgia, serif;
  }
  .card {
    position: absolute;
    top: 170px;
    width: 380px;
    height: 660px;
    background: var(--card);
    border-radius: var(--card-radius);
    overflow: hidden;
    box-shadow: 0 10px 24px rgba(0,0,0,0.35);
  }

  /* Front */
  .card--front { left: 170px; }
  .front__artwork {
    position: absolute;
    left: 0; top: 0;
    width: 190px; height: 660px;
  }
  .front__artwork svg { display: block; width: 100%; height: 100%; }
  .front__name-block {
    position: absolute;
    left: 196px;
    bottom: 36px;
    transform-origin: left bottom;
    transform: rotate(-90deg) translateY(100%);
    width: 600px;
  }
  .front__name {
    font-family: "Oswald", "Arial Narrow", sans-serif;
    font-weight: 500;
    font-size: 76px;
    line-height: 1;
    color: var(--brand-blue);
    text-transform: uppercase;
    white-space: nowrap;
  }
  .front__role {
    font-family: "Crimson Text", Georgia, serif;
    font-size: 30px;
    letter-spacing: 4px;
    color: var(--ink);
    text-transform: uppercase;
    line-height: 1.1;
    margin-top: 2px;
  }

  /* Back */
  .card--back { left: 650px; }
  .back__tagline {
    position: absolute;
    top: 128px; left: 0; right: 0;
    text-align: center;
    font-family: "Oswald", "Arial Narrow", sans-serif;
    font-weight: 300;
    font-size: 19px;
    letter-spacing: 3px;
    color: var(--ink);
    text-transform: uppercase;
  }
  .back__brand {
    position: absolute;
    top: 180px; left: 0; right: 0;
    display: flex;
    flex-direction: column;
    align-items: center;
    gap: 22px;
  }
  .back__brand-mark {
    width: 110px; height: 110px;
    border-radius: 50%;
    background: var(--ink);
  }
  .back__brand-name {
    font-family: "Oswald", "Arial Narrow", sans-serif;
    font-weight: 500;
    font-size: 54px;
    line-height: 1.05;
    color: var(--ink);
    text-transform: uppercase;
    text-align: center;
  }
  .back__contact-band {
    position: absolute;
    left: 0; right: 0; bottom: 0;
    height: 190px;
    background: var(--brand-blue);
    padding: 30px 26px 0;
    display: flex;
    flex-direction: column;
    gap: 12px;
  }
  .contact-row {
    display: flex;
    align-items: center;
    gap: 16px;
    color: var(--on-blue);
    font-size: 24px;
    line-height: 1;
    white-space: nowrap;
  }
  .contact-row svg { flex: none; }
</style>
</head>
<body>

  <section class="card card--front" aria-label="Business card front">
    <div class="front__artwork" role="img" aria-label="Black and white illustration of a Doberman in profile wearing a chain collar with a paw tag">
      <svg viewBox="0 0 190 660" preserveAspectRatio="none" aria-hidden="true">
        <defs>
          <linearGradient id="artwork-tone" x1="0" y1="0" x2="0" y2="1">
            <stop offset="0" stop-color="var(--ink-soft)"/>
            <stop offset="1" stop-color="var(--ink)"/>
          </linearGradient>
        </defs>
        <path d="M0 90 C60 95 100 150 130 260 C160 370 180 480 190 560 L190 660 L0 660 Z" fill="url(#artwork-tone)"/>
      </svg>
    </div>
    <div class="front__name-block">
      <p class="front__name">Lorna Whitfield</p>
      <p class="front__role">Dog Trainer</p>
    </div>
  </section>

  <section class="card card--back" aria-label="Business card back">
    <p class="back__tagline">Your Dog Trainer For Life</p>
    <div class="back__brand">
      <span class="back__brand-mark" aria-hidden="true"></span>
      <p class="back__brand-name">Brisa Canine<br>Coaching</p>
    </div>

    <div class="back__contact-band">
      <p class="contact-row">
        <svg width="34" height="28" viewBox="0 0 34 28" aria-hidden="true">
          <path d="M0 0H26L34 14L26 28H0Z" fill="#fff"/>
          <path d="M9 7c1-1 2-1 3 0l2 3-2 2c1 2 2 3 4 4l2-2 3 2c1 1 1 2 0 3-2 2-5 1-8-2s-5-7-4-10z" fill="var(--brand-blue)"/>
        </svg>
        <span>555-304-7719</span>
      </p>
      <p class="contact-row">
        <svg width="34" height="28" viewBox="0 0 34 28" aria-hidden="true">
          <path d="M0 0H26L34 14L26 28H0Z" fill="#fff"/>
          <text x="14" y="19" text-anchor="middle" font-size="15" font-family="Arial, sans-serif" font-weight="700" fill="var(--brand-blue)">@</text>
        </svg>
        <span>info@brisacanine.example</span>
      </p>
      <p class="contact-row">
        <svg width="34" height="28" viewBox="0 0 34 28" aria-hidden="true">
          <path d="M0 0H26L34 14L26 28H0Z" fill="#fff"/>
          <g fill="none" stroke="var(--brand-blue)" stroke-width="1.6">
            <circle cx="14" cy="14" r="7"/>
            <ellipse cx="14" cy="14" rx="3" ry="7"/>
            <line x1="7" y1="14" x2="21" y2="14"/>
          </g>
        </svg>
        <span>www.brisacanine.example</span>
      </p>
    </div>
  </section>

</body>
</html>
```